Speisekarten für ein Seerestaurant/Pizzeria
Zielgruppe
Wir sin ein Seerestaurant/Pizzeria in einem Ferien Ort
Aufgabenstellung
Wir brauchen Speisekarte in A4 und A5 Format und wichtig dass wir das Inhalt immer einfach bearbeiten können

```html
<!DOCTYPE html>
<html lang="de">
<head>
<meta charset="utf-8">
<title>Seeblick – Speisekarte</title>
<link href="https://fonts.googleapis.com/css2?family=Allura&family=Archivo+Narrow:wght@400;600&family=Roboto+Mono:wght@400&display=swap" rel="stylesheet">
<style>
  :root{
    --stage:#c0a189;
    --paper:#ffffff;
    --ink:#2a2a2a;
    --ink-soft:#4a4a4a;
    --red:#8b0a0a;
    --mist:#dfe4df;
    --script:#a9a9a9;
    --rule:#e7dcc2;
    --dot:#d8c59a;
    --url:#6b6b5f;
  }
  *{margin:0;padding:0;box-sizing:border-box}
  html,body{width:1200px;height:2296px;overflow:hidden;background:var(--stage)}
  .canvas{position:relative;width:1200px;height:2296px;background:var(--stage)}
  .page{position:absolute;width:401px;height:567px;background:var(--paper);transform-origin:0 0;
        box-shadow:0 2px 8px rgba(0,0,0,.12);font-family:"Archivo Narrow",sans-serif;color:var(--ink)}
  .page--cover{left:240px;top:90px;transform:scale(1.7955)}
  .page--starters{left:30px;top:1190px;transform:scale(1.3965)}
  .page--mains{left:610px;top:1190px;transform:scale(1.3965)}
  .abs{position:absolute}
  .mist-bar{position:absolute;left:50px;top:0;width:300px;height:8px;background:var(--mist)}
  .red-bar{position:absolute;left:50px;top:558px;width:300px;height:9px;background:var(--red)}
  .brand{position:absolute;left:0;width:100%;text-align:center}
  .brand__name{font-family:"Archivo Narrow",sans-serif;font-weight:600;color:var(--ink);letter-spacing:-.5px}
  .brand__tag{font-family:"Roboto Mono",monospace;color:var(--ink);letter-spacing:.4px}
  .footer-line{position:absolute;left:0;top:541px;width:100%;text-align:center;
       font-family:"Roboto Mono",monospace;font-size:5px;letter-spacing:.8px;color:var(--red)}
  .script{position:absolute;font-family:"Allura",cursive;color:var(--script);line-height:1;white-space:nowrap}
  .col-rule{position:absolute;width:1px;background:var(--rule)}
  .dish{position:absolute;text-align:right;white-space:nowrap}
  .dish__name{font-size:8.2px;line-height:9px;letter-spacing:.3px;color:var(--ink)}
  .dish__desc{font-size:5.4px;line-height:8.6px;color:var(--ink-soft)}
  .price{position:absolute;font-size:4.4px;line-height:6px;color:var(--ink-soft);white-space:nowrap}
  .price::before{content:"";position:absolute;left:-10px;top:2px;width:2.4px;height:2.4px;border-radius:50%;background:var(--dot)}
  .photo{position:absolute}
  .note{position:absolute;font-family:"Roboto Mono",monospace;font-size:3.8px;line-height:6.4px;letter-spacing:.3px;color:var(--ink-soft);white-space:nowrap}
  .cover__url{position:absolute;top:26px;width:100%;text-align:center;font-family:"Roboto Mono",monospace;font-size:10px;letter-spacing:1px;color:var(--url)}
  .cover__tag{position:absolute;top:393px;width:100%;text-align:center;font-family:"Roboto Mono",monospace;font-size:8.6px;letter-spacing:1.6px;color:var(--red)}
  .cover__address{position:absolute;top:412px;width:100%;text-align:center;font-family:"Roboto Mono",monospace;font-size:5.4px;letter-spacing:.6px;color:var(--ink)}
  .cover__band{position:absolute;left:50px;top:531px;width:300px;height:36px;background:var(--red);
       color:#fff;font-family:"Roboto Mono",monospace;font-size:5.8px;letter-spacing:1.6px;text-align:center;line-height:36px;word-spacing:4px}
</style>
</head>
<body>
<div class="canvas">

  <!-- Cover -->
  <section class="page page--cover">
    <div class="cover__url">seeblick-uferdorf.ch</div>
    <div class="brand" style="top:296px"><div class="brand__name" style="font-size:60px;line-height:70px">Seeblick</div></div>
    <div class="cover__tag">Seerestaurant – SEEWINKEL – Uferdorf</div>
    <div class="cover__address">Uferweg 12 • 6300 Uferdorf</div>
    <div class="cover__band">LUNCH &nbsp; | &nbsp; DINNER</div>
  </section>

  <!-- Suppen & Salate -->
  <section class="page page--starters">
    <div class="mist-bar"></div>
    <div class="brand" style="top:26px">
      <div class="brand__name" style="font-size:26px;line-height:30px">Seeblick</div>
      <div class="brand__tag" style="font-size:3.6px">Seerestaurant – SEEWINKEL – Uferdorf</div>
    </div>

    <div class="script" style="left:280px;top:98px;font-size:32px">Salate</div>
    <div class="script" style="left:98px;top:143px;font-size:32px">Suppen</div>

    <div class="col-rule" style="left:130px;top:188px;height:134px"></div>
    <div class="dish" style="right:281px;top:202px"><div class="dish__name">BOUILLON</div><div class="dish__desc">mit Tortelloni</div></div>
    <div class="dish" style="right:281px;top:233px"><div class="dish__name">GULASCHSUPPE</div><div class="dish__desc">...die Echte – nach ungarischer Art</div></div>
    <div class="dish" style="right:281px;top:265px"><div class="dish__name">MINESTRONE</div></div>
    <div class="dish" style="right:281px;top:292px"><div class="dish__name">TAGESSUPPE</div><div class="dish__desc">fragen Sie unser Personal</div></div>
    <div class="price" style="left:139px;top:205px">CHF 10.50</div>
    <div class="price" style="left:139px;top:236px">kl. Portion CHF 13.50<br>kl. Portion CHF 20.50</div>
    <div class="price" style="left:139px;top:268px">CHF 11.50</div>
    <div class="price" style="left:139px;top:295px">CHF 11.50</div>

    <div class="col-rule" style="left:312px;top:135px;height:210px"></div>
    <div class="dish" style="right:100px;top:145px"><div class="dish__name">BURRATA</div><div class="dish__desc">italienischer Frischkäse, mit frischem<br>Basilikum, extra natives Olivenöl,<br>Balsamico Crema und Cherry Tomaten</div></div>
    <div class="dish" style="right:100px;top:189px"><div class="dish__name">CEASAR SALAT</div><div class="dish__desc">mit Speck, Croûtons und Parmigiano DOP</div></div>
    <div class="dish" style="right:100px;top:215px"><div class="dish__name">FITNESSTELLER</div><div class="dish__desc">mit Pouletstreifen</div></div>
    <div class="dish" style="right:100px;top:241px"><div class="dish__name">GEMISCHTER SALAT</div></div>
    <div class="dish" style="right:100px;top:259px"><div class="dish__name">GRÜNER SALAT</div></div>
    <div class="dish" style="right:100px;top:277px"><div class="dish__name">NÜSSLISALAT</div><div class="dish__desc">mit Speck, Brotcroûtons und Ei</div></div>
    <div class="dish" style="right:100px;top:303px"><div class="dish__name">SALAT «SEEWINKEL»</div><div class="dish__desc">Eisberg Salat, Speck, Croutons,<br>Parmigiano DOP und Pouletstreifen</div></div>
    <div class="price" style="left:321px;top:148px">CHF 17.00</div>
    <div class="price" style="left:321px;top:192px">CHF 14.50</div>
    <div class="price" style="left:321px;top:218px">CHF 11.50</div>
    <div class="price" style="left:321px;top:244px">CHF 11.50</div>
    <div class="price" style="left:321px;top:262px">CHF 11.50</div>
    <div class="price" style="left:321px;top:280px">CHF 14.50</div>
    <div class="price" style="left:321px;top:306px">CHF 28.50</div>

    <svg class="photo" style="left:76px;top:361px" width="96" height="134" role="img" aria-label="Foto: Burrata auf Tomatensalat mit Basilikum">
      <defs><linearGradient id="gBurrata" x1="0" y1="0" x2="0" y2="1"><stop offset="0" stop-color="#3f4448"/><stop offset=".45" stop-color="#e9e6e1"/><stop offset="1" stop-color="#b8332b"/></linearGradient></defs>
      <rect width="96" height="134" fill="url(#gBurrata)"/>
    </svg>
    <div class="note" style="right:78px;top:404px;text-align:right">MIT HAUSGEMACHTER SALATSAUCE<br>IHRER WAHL UND FRISCHEM PIZZABROT</div>
    <svg class="photo" style="left:189px;top:430px" width="134" height="96" role="img" aria-label="Foto: Salat mit gebratenen Pouletstreifen">
      <defs><linearGradient id="gSalad" x1="0" y1="0" x2="1" y2="1"><stop offset="0" stop-color="#d9b98a"/><stop offset=".5" stop-color="#c48a4a"/><stop offset="1" stop-color="#6f8a3a"/></linearGradient></defs>
      <rect width="134" height="96" fill="url(#gSalad)"/>
    </svg>

    <div class="footer-line">Seerestaurant – SEEWINKEL – Uferdorf</div>
    <div class="red-bar"></div>
  </section>

  <!-- Hauptgerichte & Barbecue -->
  <section class="page page--mains">
    <div class="mist-bar"></div>
    <div class="brand" style="top:26px">
      <div class="brand__name" style="font-size:26px;line-height:30px">Seeblick</div>
      <div class="brand__tag" style="font-size:3.6px">Seerestaurant – SEEWINKEL – Uferdorf</div>
    </div>

    <div class="script" style="left:108px;top:84px;font-size:36px">Hauptgerichte</div>

    <div class="col-rule" style="left:190px;top:135px;height:180px"></div>
    <div class="dish" style="right:222px;top:134px"><div class="dish__name">BEEFSTEAK TARTAR</div><div class="dish__desc">aus Schweizer-Qualitätsrindfleisch abgeschmeckt nacht<br>Ihrem Wunsch, serviert mit Toastbrot und Butter</div></div>
    <div class="dish" style="right:222px;top:169px"><div class="dish__name">CHICKEN-FINGERS</div><div class="dish__desc">hausgemachte, panierte Pouletstreifen,<br>dazu sweet Chili-Sauce und Pommes Frites</div></div>
    <div class="dish" style="right:222px;top:204px"><div class="dish__name">CORDON BLEU</div><div class="dish__desc">«das Klassische» vom Schwein, gefüllt mit Vorderschinken,<br>Raclette und würzigem Gruyère serviert mit Pommes Frites<br>und Gemüse</div></div>
    <div class="dish" style="right:222px;top:248px"><div class="dish__name">GYROS-TELLER</div><div class="dish__desc">mit Schweinefleisch serviert mit Salat-Bouquet,<br>Tzatziki-Sauce und Pommes Frites</div></div>
    <div class="dish" style="right:222px;top:283px"><div class="dish__name">WIENER SCHNITZEL</div><div class="dish__desc">vom Kalb mit Pommes Frites und Preiselbeeren</div></div>
    <div class="price" style="left:199px;top:136px">Vorspeise CHF 22.50 &nbsp;|&nbsp; Hauptgang CHF 32.50</div>
    <div class="price" style="left:199px;top:171px">CHF 26.50</div>
    <div class="price" style="left:199px;top:206px">CHF 32.50</div>
    <div class="price" style="left:199px;top:250px">CHF 30.50</div>
    <div class="price" style="left:199px;top:285px">CHF 35.50</div>

    <svg class="photo" style="left:241px;top:161px" width="134" height="96" role="img" aria-label="Foto: Spare Ribs mit Kartoffelecken und Dip">
      <defs><linearGradient id="gRibs" x1="0" y1="0" x2="0" y2="1"><stop offset="0" stop-color="#1d1714"/><stop offset=".55" stop-color="#6b3320"/><stop offset="1" stop-color="#3a2418"/></linearGradient></defs>
      <rect width="134" height="96" fill="url(#gRibs)"/>
    </svg>

    <div class="script" style="left:280px;top:268px;font-size:26px">Barbecue</div>
    <div class="script" style="left:258px;top:293px;font-size:26px">Spezialitäten</div>
    <div class="abs" style="left:277px;top:331px;font-size:7.4px;letter-spacing:.4px">AUS DEM SMOKER</div>

    <svg class="photo" style="left:27px;top:340px" width="134" height="96" role="img" aria-label="Foto: Pulled Pork Burger mit Pommes Frites">
      <defs><linearGradient id="gBurger" x1="0" y1="0" x2="1" y2="1"><stop offset="0" stop-color="#5a5048"/><stop offset=".5" stop-color="#b0703a"/><stop offset="1" stop-color="#d8c7a8"/></linearGradient></defs>
      <rect width="134" height="96" fill="url(#gBurger)"/>
    </svg>
    <div class="note" style="left:27px;top:447px">BARBECUE GERICHTE WERDEN<br>6-12 STUNDEN IM SMOKER GEGART.</div>
    <div class="note" style="left:27px;top:467px">WIR VERWENDEN AUSSCHLIESSLICH<br>SCHWEIZER FLEISCH UND BIO HICKORY<br>HOLZ FÜR DAS TYPISCHE BBQ ERLEBNIS<br>UND RAUCH-AROMA.</div>

    <div class="col-rule" style="left:313px;top:352px;height:166px"></div>
    <div class="dish" style="right:99px;top:363px"><div class="dish__name">BBQ SPARE RIBS</div><div class="dish__desc">aus dem Smoker mit Cherry-Bomb Glasur<br>serviert mit Pommes frites</div></div>
    <div class="dish" style="right:99px;top:398px"><div class="dish__name">PULLED BEEF Burger</div><div class="dish__desc">Hausgemachte Bun, Pulled Beef (180g), BBQ-Sauce,<br>Cheddar-Käse, Coleslaw (Kabissalat) und Jalapeno,<br>serviert mit Pommes</div></div>
    <div class="dish" style="right:99px;top:442px"><div class="dish__name">PULLED PORK Burger</div><div class="dish__desc">Hausgemachte Bun, Pulled Pork (180g), BBQ-Sauce,<br>Cheddar-Käse, Coleslaw (Kabissalat) und Jalapeno,<br>serviert mit Pommes</div></div>
    <div class="dish" style="right:99px;top:486px"><div class="dish__name">PULLED VEGI Burger</div><div class="dish__desc">Hausgemachte Bun, BBQ-Sauce, Cheddar-Käse, Coleslaw<br>(Kabissalat) und Jalapeno, serviert mit Pommes</div></div>
    <div class="price" style="left:322px;top:365px">CHF 44.00</div>
    <div class="price" style="left:322px;top:400px">CHF 31.50</div>
    <div class="price" style="left:322px;top:444px">CHF 28.50</div>
    <div class="price" style="left:322px;top:488px">CHF 25.50</div>

    <div class="footer-line">Seerestaurant – SEEWINKEL – Uferdorf</div>
    <div class="red-bar"></div>
  </section>

</div>
</body>
</html>
```